Cover Page for our 2021 Comprehensive Needs Assessment Report 3 ring binder

Create a cover for our 2021 Comprehensive Needs Assessment. This is a report full of survey and non survey data, used for decision making. Modern Colors. Logo is attached as well as 2020 cover for easy explanation. However we do not want the same cover as last year, it should have a new color scheme for this year and a new look with the same feel.

Target Market(s)

School Districts

```html
<!DOCTYPE html>
<html lang="en">
<head>
<meta charset="utf-8">
<title>2021 Needs Assessment Cover</title>
<link rel="stylesheet" href="https://fonts.googleapis.com/css2?family=Bebas+Neue&family=Comfortaa:wght@700&family=Open+Sans:wght@400;600&display=swap">
<style>
  :root {
    --backdrop: #717275;
    --paper: #ffffff;
    --charcoal: #394043;
    --charcoal-deep: #232a2c;
    --sun: #fcb813;
    --amber: #f7941d;
    --lime: #8cc63f;
    --green: #3fb549;
    --ink: #222222;
    --scene-top: #e9dcef;
    --scene-mid: #f4b64a;
    --scene-low: #6b3b8e;
  }
  * { margin: 0; padding: 0; box-sizing: border-box; }
  html, body { width: 1200px; height: 1200px; overflow: hidden; background: var(--backdrop); }
  .cover {
    position: absolute; left: 362px; top: 264px;
    width: 595px; height: 842px;
    transform: scale(0.8); transform-origin: top left;
    background: var(--paper); overflow: hidden;
    font-family: "Open Sans", sans-serif;
  }
  .cover-shapes { position: absolute; inset: 0; }
  .intro {
    position: absolute; left: 27px; top: 26px; width: 360px;
    font-size: 9px; line-height: 14px; color: var(--ink);
  }
  .brand {
    position: absolute; left: 432px; top: 30px; width: 150px;
    display: flex; align-items: center; gap: 6px;
    font-family: "Open Sans", sans-serif; font-weight: 600;
    font-size: 13px; line-height: 16px; color: var(--ink);
  }
  .brand-dot { width: 12px; height: 12px; border-radius: 50%; background: var(--lime); flex: none; }
  .year {
    position: absolute; left: 396px; top: 436px;
    font-family: "Comfortaa", sans-serif; font-weight: 700;
    font-size: 54px; color: var(--green); letter-spacing: 1px;
  }
  .title { position: absolute; left: 40px; top: 562px; font-family: "Bebas Neue", sans-serif; }
  .title-kicker { display: block; font-size: 34px; line-height: 34px; letter-spacing: 7px; color: var(--lime); }
  .title-main { display: block; font-size: 66px; line-height: 58px; color: var(--sun); }
  .title-sub { display: block; font-size: 66px; line-height: 58px; color: var(--lime); }
  .contacts {
    position: absolute; left: 128px; top: 750px;
    display: flex; gap: 14px;
  }
  .contact { width: 100px; display: flex; flex-direction: column; align-items: center; gap: 8px; }
  .contact svg { width: 28px; height: 28px; }
  .contact span { font-size: 9px; color: var(--paper); white-space: nowrap; }
</style>
</head>
<body>
  <div class="cover">
    <svg class="cover-shapes" viewBox="0 0 595 842" width="595" height="842" aria-hidden="false">
      <defs>
        <linearGradient id="sceneTone" x1="0" y1="0" x2="1" y2="1">
          <stop offset="0" stop-color="var(--scene-top)"/>
          <stop offset="0.55" stop-color="var(--scene-mid)"/>
          <stop offset="1" stop-color="var(--scene-low)"/>
        </linearGradient>
        <linearGradient id="sunBand" x1="0" y1="0" x2="1" y2="0">
          <stop offset="0" stop-color="var(--sun)"/>
          <stop offset="1" stop-color="var(--amber)"/>
        </linearGradient>
        <linearGradient id="glow" x1="0" y1="0" x2="0" y2="1">
          <stop offset="0" stop-color="#ffffff"/>
          <stop offset="1" stop-color="#fbc47c"/>
        </linearGradient>
      </defs>
      <polygon role="img" aria-label="Isometric illustration of a modern learning space with students working at desks and relaxing in hammocks"
        points="0,72 595,72 595,380 430,440 250,462 0,420" fill="url(#sceneTone)"/>
      <polygon points="175,78 595,84 595,138" fill="url(#sunBand)"/>
      <polygon points="170,76 595,80 595,86" fill="var(--charcoal)"/>
      <polygon points="0,430 595,615 595,842 0,842" fill="var(--charcoal)"/>
      <polygon points="525,525 595,380 595,615 525,600" fill="url(#glow)"/>
      <polygon points="0,440 538,620 538,682 0,450" fill="var(--charcoal-deep)"/>
      <polygon points="0,420 525,525 525,645 0,440" fill="url(#sunBand)"/>
    </svg>

    <p class="intro">Lorem ipsum dolor sit amet consectetue adipiscing elit,sed do eiusmod tempor incididunt ut labore et dolore magna aliqua. Ut enim ad minim veniam. Lorem</p>

    <div class="brand"><span class="brand-dot"></span><span>Learning Pathways Group</span></div>

    <div class="year">2021</div>

    <h1 class="title">
      <span class="title-kicker">Full Report of</span>
      <span class="title-main">Survey and</span>
      <span class="title-sub">Non Survey Data</span>
    </h1>

    <div class="contacts">
      <div class="contact">
        <svg viewBox="0 0 28 28"><circle cx="14" cy="14" r="12.5" fill="none" stroke="#fff" stroke-width="2"/><rect x="7.5" y="9.5" width="13" height="9" fill="none" stroke="#fff" stroke-width="1.4"/><path d="M7.5 9.5 14 15l6.5-5.5M7.5 18.5l5-4.5M20.5 18.5l-5-4.5" fill="none" stroke="#fff" stroke-width="1.2"/></svg>
        <span>LOREM IPSUM DOLOR</span>
      </div>
      <div class="contact">
        <svg viewBox="0 0 28 28"><circle cx="14" cy="14" r="13" fill="#fff"/><path d="M7 14.5 14 8l7 6.5h-2v5.5h-3.5v-4h-3v4H9v-5.5z" fill="var(--charcoal)"/></svg>
        <span>LOREM IPSUM DOLOR</span>
      </div>
      <div class="contact">
        <svg viewBox="0 0 28 28"><circle cx="14" cy="14" r="13" fill="#fff"/><circle cx="14" cy="14" r="8" fill="var(--charcoal)"/><path d="M10.5 11c0 4 2.5 6.5 6.5 6.5l1-1.6-2-1.2-1 .9c-1.2-.5-2-1.3-2.6-2.6l.9-1-1.2-2z" fill="#fff"/></svg>
        <span>LOREM IPSUM DOLOR</span>
      </div>
    </div>
  </div>
</body>
</html>
```